Lorne Hollow Farm Postcard Design

I am looking for a new postcard design to mail out this season. We are a Farm business that does wholesale and retail and bulk seasoned firewood sales. we sell firewood from anything from bagged wood to tractor trailer loads of wood. We sell firewood in bulk bags. Pick up or delivery available there is no order to big or too small. I need my business name and phone number on the cards Lorne Hollow Farm 848-316-0572 (call or text) I would like it to say we are the best priced guaranteed. I want something that is simple and straight forward but also really catches the eye when they see these in the mail box. I attached my logo and feel free to use photos of split firewood if you would like. id like my email on the card Lornehollowfarm90@mailvista.net.

Target Market(s)

Firewood purchasers

Industry/Entity Type

agriculture

Requirements
Must have
• email phone number logo

```html
<!DOCTYPE html>
<html lang="en">
<head>
<meta charset="utf-8">
<title>Lorne Hollow Farm Postcard</title>
<link href="https://fonts.googleapis.com/css2?family=Poppins:wght@600;800;900&family=Oswald:wght@500;600&display=swap" rel="stylesheet">
<style>
:root{
  --page:#d0d0d0;
  --ink:#111010;
  --white:#ffffff;
  --gold:#fbbf2e;
  --ribbon:#e2562f;
  --flame-red:#ec3b3b;
  --flame-orange:#f6891f;
  --flame-yellow:#fcc63a;
  --bar:#d9d9d9;
  --wood-dark:#3a2a1e;
  --wood-mid:#9a6332;
  --wood-light:#c98e4c;
}
*{margin:0;padding:0;box-sizing:border-box}
html,body{width:1200px;height:1200px;overflow:hidden;background:var(--page)}
body{position:relative;font-family:"Poppins",sans-serif}
.card{position:absolute;overflow:hidden}
.card-front{left:73px;top:59px;width:718px;height:520px;background:var(--ink)}
.card-back{left:373px;top:624px;width:719px;height:521px;background:var(--white)}
.header{position:absolute;left:0;top:0;width:718px;height:160px;background:linear-gradient(90deg,#1a1410,#0d0c0b 60%,#1b140e)}
.brand{position:absolute;text-align:center;color:var(--flame-orange);font-weight:800;line-height:1.05}
.brand-name{font-size:20px;letter-spacing:.3px}
.brand-mark{display:inline-block;width:12px;height:12px;border-radius:50%;background:var(--flame-orange);margin-bottom:6px}
.brand-sub{font-size:8px;letter-spacing:1.2px;margin-top:4px}
.headline{position:absolute;left:208px;top:20px;font-weight:900;font-size:36px;line-height:37px;color:var(--white);letter-spacing:-.5px;text-transform:uppercase}
.headline .accent{color:var(--gold)}
.saw-bar{position:absolute;left:206px;top:106px;width:464px;height:26px;background:var(--bar);border-radius:2px 14px 14px 2px;clip-path:polygon(0 0,100% 0,100% 100%,4% 100%,0 85%)}
.saw-bar span{position:absolute;left:46px;right:16px;top:3px;font-family:"Oswald",sans-serif;font-weight:500;font-style:italic;font-size:12.4px;line-height:20px;color:var(--ink);white-space:nowrap;letter-spacing:-.25px;text-align:left}
.saw-tab{position:absolute;left:206px;top:100px;width:40px;height:36px;background:var(--flame-orange);border-radius:6px}
.photo{position:absolute}
.firewood{left:0;top:150px;width:718px;height:300px;background:linear-gradient(115deg,var(--wood-dark) 0%,var(--wood-mid) 22%,var(--wood-light) 40%,var(--wood-mid) 58%,var(--wood-light) 75%,var(--wood-dark) 100%)}
.ribbon{position:absolute;width:130px}
.ribbon-drop{position:absolute;left:10px;top:0;width:110px;height:100px;background:var(--gold);clip-path:polygon(0 0,100% 0,100% 100%,50% 84%,0 100%)}
.ribbon-band{position:absolute;left:0;top:26px;width:130px;height:22px;background:var(--ribbon);color:var(--white);font-weight:800;font-size:15px;text-align:center;line-height:22px}
.ribbon-text{position:absolute;left:0;top:50px;width:130px;text-align:center;font-family:"Oswald",sans-serif;font-weight:600;font-size:19px;color:var(--ink)}
.circle{position:absolute;width:132px;height:132px;border-radius:50%;border:3px solid var(--white);box-shadow:0 0 0 6px rgba(252,198,58,.55)}
.circle-chop{left:428px;top:320px;background:linear-gradient(160deg,#5f6e44 0%,#a5895e 55%,#3d3a36 100%)}
.circle-truck{left:545px;top:320px;background:linear-gradient(160deg,#9aa2ab 0%,#c2602a 55%,#4a3b30 100%)}
.flame-band{position:absolute;left:0;top:440px;width:718px;height:80px;background:linear-gradient(90deg,var(--flame-red),var(--flame-orange) 55%,var(--flame-yellow))}
.contact{position:absolute;color:var(--white);display:flex;align-items:center;gap:8px}
.contact svg{flex:none}
.contact-label{font-weight:800;font-size:13px;letter-spacing:.6px;line-height:14px}
.contact-value{font-weight:800;font-size:22px;line-height:24px;letter-spacing:.3px}
.tear{position:absolute;left:0;width:100%}
.forest{left:0;top:0;width:428px;height:235px;background:linear-gradient(180deg,#3f5e56 0%,#4d5f3c 40%,#8b6a3e 72%,#4a3a2a 100%)}
.back-dark{position:absolute;left:0;top:232px;width:428px;height:289px;background:#151210}
.logs{left:0;top:260px;width:217px;height:112px;background:linear-gradient(90deg,#4a2a1c 0%,#7a3f26 50%,#b5683a 85%,#6b3522 100%)}
.address-side{position:absolute;left:428px;top:0;width:291px;height:521px;background:var(--white)}
.stamp-box{position:absolute;left:630px;top:16px;width:73px;height:84px;border:1px solid #8a8a8a}
</style>
</head>
<body>

<section class="card card-front">
  <div class="header"></div>
  <div class="brand" style="left:22px;top:34px;width:140px">
    <span class="brand-mark"></span>
    <div class="brand-name">Lorne Hollow Farm</div>
    <div class="brand-sub">732-505-0184</div>
  </div>
  <h1 class="headline">Quality Firewood<br>Deliver <span class="accent">at your door!</span></h1>
  <div class="saw-bar"><span>PICK UP OR DELIVERY AVAILABLE THERE IS NO ORDER TO BIG OR TOO SMALL</span></div>
  <div class="saw-tab"></div>

  <div class="photo firewood" role="img" aria-label="Close-up photo of stacked split firewood with autumn leaves"></div>
  <svg class="tear" style="top:146px" height="14" viewBox="0 0 718 14" preserveAspectRatio="none"><path d="M0 6 L20 3 L38 8 L60 4 L90 7 L120 2 L150 6 L185 3 L215 8 L250 4 L290 7 L330 3 L370 6 L410 2 L450 7 L490 4 L530 8 L570 3 L610 6 L650 2 L690 7 L718 4 L718 14 L0 14 Z" fill="#0d0c0b"/><path d="M0 6 L20 3 L38 8 L60 4 L90 7 L120 2 L150 6 L185 3 L215 8 L250 4 L290 7 L330 3 L370 6 L410 2 L450 7 L490 4 L530 8 L570 3 L610 6 L650 2 L690 7 L718 4" fill="none" stroke="#fff" stroke-width="3"/></svg>

  <div class="ribbon" style="left:36px;top:155px">
    <div class="ribbon-drop"></div>
    <div class="ribbon-band">BEST PRICE</div>
    <div class="ribbon-text">GUARANTEED</div>
  </div>

  <div class="flame-band"></div>
  <svg class="tear" style="top:434px" height="14" viewBox="0 0 718 14" preserveAspectRatio="none"><path d="M0 8 L30 5 L60 9 L95 4 L130 8 L170 5 L210 9 L250 4 L290 8 L330 5 L370 9 L410 4 L450 8 L490 5 L530 9 L570 4 L610 8 L650 5 L690 9 L718 5" fill="none" stroke="#fff" stroke-width="3"/></svg>

  <div class="circle circle-chop" role="img" aria-label="Photo of a person splitting wood with an axe"></div>
  <div class="circle circle-truck" role="img" aria-label="Photo of an orange log truck loaded with timber"></div>

  <div class="contact" style="left:32px;top:460px">
    <svg width="42" height="40" viewBox="0 0 42 40"><polygon points="11,2 31,2 40,20 31,38 11,38 2,20" fill="none" stroke="#fff" stroke-width="2"/><path d="M15 12 q-3 2 0 9 q4 8 10 8 l3 -3 l-4 -4 l-2 2 q-4 -2 -5 -6 l2 -2 l-3 -5 Z" fill="#fff"/></svg>
    <div><div class="contact-label">CALL OR TEXT</div><div class="contact-value">848-316-0572</div></div>
  </div>
  <div class="contact" style="left:283px;top:460px">
    <svg width="42" height="40" viewBox="0 0 42 40"><polygon points="11,2 31,2 40,20 31,38 11,38 2,20" fill="none" stroke="#fff" stroke-width="2"/><rect x="12" y="13" width="18" height="13" fill="none" stroke="#fff" stroke-width="1.5"/><path d="M12 13 L21 21 L30 13 M12 26 L18 19 M30 26 L24 19" fill="none" stroke="#fff" stroke-width="1.3"/></svg>
    <div><div class="contact-label">EMAIL US AT</div><div class="contact-value" style="font-size:19px">Lornehollowfarm90@mailvista.net</div></div>
  </div>
</section>

<section class="card card-back">
  <div class="photo forest" role="img" aria-label="Photo of a yellow wheel loader moving logs in a muddy forest clearing"></div>
  <div class="back-dark"></div>
  <svg class="tear" style="top:228px;width:428px" height="12" viewBox="0 0 428 12" preserveAspectRatio="none"><path d="M0 6 L25 3 L50 8 L80 4 L110 7 L140 3 L170 8 L200 4 L230 7 L260 3 L290 8 L320 4 L350 7 L380 3 L410 7 L428 4" fill="none" stroke="#fff" stroke-width="3"/></svg>
  <div class="photo logs" role="img" aria-label="Photo of a stack of cut logs"></div>

  <div class="ribbon" style="left:272px;top:230px">
    <div class="ribbon-drop"></div>
    <div class="ribbon-band">BEST PRICE</div>
    <div class="ribbon-text">GUARANTEED</div>
  </div>

  <div class="brand" style="left:270px;top:360px;width:135px">
    <span class="brand-mark"></span>
    <div class="brand-name" style="font-size:19px">Lorne Hollow Farm</div>
    <div class="brand-sub">732-505-0184</div>
  </div>

  <div class="contact" style="left:32px;top:408px">
    <svg width="42" height="40" viewBox="0 0 42 40"><polygon points="11,2 31,2 40,20 31,38 11,38 2,20" fill="none" stroke="#fff" stroke-width="2"/><path d="M15 12 q-3 2 0 9 q4 8 10 8 l3 -3 l-4 -4 l-2 2 q-4 -2 -5 -6 l2 -2 l-3 -5 Z" fill="#fff"/></svg>
    <div><div class="contact-label">CALL OR TEXT</div><div class="contact-value">848-316-0572</div></div>
  </div>
  <div class="contact" style="left:32px;top:458px">
    <svg width="42" height="40" viewBox="0 0 42 40"><polygon points="11,2 31,2 40,20 31,38 11,38 2,20" fill="none" stroke="#fff" stroke-width="2"/><rect x="12" y="13" width="18" height="13" fill="none" stroke="#fff" stroke-width="1.5"/><path d="M12 13 L21 21 L30 13 M12 26 L18 19 M30 26 L24 19" fill="none" stroke="#fff" stroke-width="1.3"/></svg>
    <div><div class="contact-label">EMAIL US AT</div><div class="contact-value" style="font-size:17px">Lornehollowfarm90@mailvista.net</div></div>
  </div>

  <div class="address-side"></div>
  <div class="stamp-box"></div>
</section>

</body>
</html>
```